Personal Finance Author needs a postcard

Hi there,

I am a Canadian personal finance author and have published a new book called The Wealth Compass.

I teach Millennials how to create a 6-figure portfolio through investing (https://www.dariafelt.com/)

I'm speaking at some conferences so we were going to print some postcards to hand out to attendees with our info and calls-to-action on them.

I am looking for 4x6 (horizontal) postcard (no space needed for shipping label).

Logos, Headshots and Book Cover:
https://files.cloudvaultex.com/folders/8kQpZrT2mWvN4xLbJ7sHdYc3FgA9eUoRi?usp=sharing

Both sides will be full colour. I would like a clean and simple look. Our main sites are www.DariaFelt.com and www.TheWealthCompassBook.com if you want to get a sense of style and design.
I also uploaded a few marketing materials so you can see the existing designs.

Side 1:
Get Instant Access to your Free Resources - main headline

(small bullets underneath)
- The Wealth Compass Checklist
- Financial Worksheets
- Database of Investment Tools

DariaFelt.com/Resources

At the bottom, include "Don't forget to follow Daria Felt on social media:
Linkedin: @dariafelt7
Facebook: @thewealthcompassbook Instagram: @thewealthcompassbook Twitter: @WealthCompassBk"

Side 2:
Headline - Want to work directly with Daria and The Wealth Compass team to help you make your money grow and stay safe?

Work with us to (bullet point list)...
- Hire Daria as a Keynote Speaker
- Teach Financial Literacy Workshops
- Receive Financial Coaching

Want To Learn More About How We Can Help?
DariaFelt.com/Services

Include my contact info:
Daria Felt
Author | Speaker | Investor
daria@thewealthcompassbook.com
416-555-0187

Target Market(s)

Millennials who want to learn how to save and invest their money. I focus on stock market investing, real estate investing and entrepreneurship.

Industry/Entity Type

Financial Service

Font styles to use
Sans Serif

Colors

Designer to choose colors to be used in the design.

Requirements
Must have
• Photo of Daria Felt
• The Wealth Compass logo
• Green, Gold/Yellow to match existing colours
• modern business style postcard

```html
<!DOCTYPE html>
<html lang="en">
<head>
<meta charset="utf-8">
<title>The Wealth Compass – Postcard</title>
<link rel="stylesheet" href="https://fonts.googleapis.com/css2?family=Montserrat:wght@400;600;700&family=Montserrat+Alternates:ital,wght@0,400;1,400;1,600;1,700&family=Didact+Gothic&display=swap">
<style>
  :root {
    --canvas: #b4b4b4;
    --paper-light: #f6f6f6;
    --paper-mid: #e2e2e2;
    --ink: #2b2b2b;
    --green-dark: #063a21;
    --green: #0b5a33;
    --gold: #f0a81c;
    --gold-light: #ffd36a;
    --white: #ffffff;
  }
  * { box-sizing: border-box; margin: 0; padding: 0; }
  html, body { width: 1200px; height: 1200px; overflow: hidden; }
  body {
    background: var(--canvas);
    display: flex; flex-direction: column; align-items: center; justify-content: center;
    gap: 40px;
    font-family: "Didact Gothic", sans-serif;
    color: var(--ink);
  }
  .postcard {
    position: relative; width: 810px; height: 540px; overflow: hidden;
    background: radial-gradient(ellipse at 60% 40%, var(--paper-light), var(--paper-mid));
    box-shadow: 0 8px 24px rgba(0,0,0,.25);
  }
  .band {
    position: absolute; left: 0; right: 0; bottom: 0;
    background: linear-gradient(180deg, var(--green) 0%, var(--green-dark) 100%);
    border-top: 10px solid var(--gold);
    box-shadow: 0 -3px 0 var(--gold-light) inset;
  }
  /* Front */
  .front .band { height: 175px; }
  .book-cover {
    position: absolute; left: 40px; top: 130px; width: 300px; height: 380px;
    background: linear-gradient(160deg, #fafafa 0%, #e9e9e9 55%, var(--green) 100%);
    box-shadow: 6px 8px 18px rgba(0,0,0,.35);
  }
  .offer { position: absolute; right: 40px; top: 40px; width: 420px; text-align: right; }
  .headline {
    font-family: "Montserrat", sans-serif; font-weight: 700;
    font-size: 27px; letter-spacing: 2.5px; line-height: 1.25; text-transform: uppercase;
  }
  .rule { height: 2px; background: var(--ink); margin: 16px 0 20px 30px; }
  .resource-list { list-style: none; font-size: 21px; line-height: 1; }
  .resource-list li { display: flex; justify-content: flex-end; align-items: center; gap: 12px; margin-bottom: 18px; }
  .tick { width: 18px; height: 14px; flex: none; }
  .offer .rule.bottom { margin: 4px 0 0 30px; }
  .resources-url { margin-top: 34px; font-size: 16px; }
  .social { position: absolute; left: 370px; right: 40px; bottom: 24px; color: var(--white); }
  .social-title { font-family: "Montserrat", sans-serif; font-size: 12px; font-weight: 600; letter-spacing: .5px; margin-bottom: 14px; text-transform: uppercase; }
  .social-grid { display: grid; grid-template-columns: 1fr 1fr; gap: 10px 20px; font-size: 14px; }
  .social-item { display: flex; align-items: center; gap: 10px; }
  .social-dot { width: 13px; height: 13px; border-radius: 50%; background: var(--white); flex: none; }
  /* Back */
  .back .band { height: 190px; }
  .pitch { position: absolute; left: 40px; top: 32px; width: 470px; font-family: "Montserrat Alternates", sans-serif; }
  .pitch-headline { font-style: italic; font-size: 22px; line-height: 1.15; }
  .pitch-label { font-size: 9px; letter-spacing: 3px; text-transform: uppercase; margin: 16px 0 6px; font-style: italic; }
  .service-list { list-style: none; font-style: italic; font-weight: 700; font-size: 14px; line-height: 1.35; }
  .service-list li::before { content: "- "; }
  .services-cta { margin-top: 16px; font-size: 9px; letter-spacing: 3px; text-transform: uppercase; font-style: italic; }
  .services-url { font-size: 11px; font-style: italic; }
  .contact { position: absolute; left: 40px; bottom: 40px; color: var(--white); font-family: "Montserrat Alternates", sans-serif; font-style: italic; }
  .contact-name { font-weight: 700; font-size: 22px; }
  .contact-role { font-size: 11px; font-weight: 600; margin-bottom: 8px; }
  .contact-line { font-size: 13px; line-height: 1.35; }
  .brand-name {
    position: absolute; left: 330px; bottom: 50px; width: 170px;
    font-family: "Montserrat", sans-serif; font-weight: 700; font-size: 22px; line-height: 1.05;
    color: var(--gold); text-transform: uppercase; text-align: center;
  }
  .portrait {
    position: absolute; right: 30px; top: 110px; width: 270px; height: 430px;
    background: linear-gradient(180deg, #c9a58c 0%, #1d1d22 45%, #121215 100%);
  }
</style>
</head>
<body>

<section class="postcard front">
  <div class="band"></div>
  <div class="book-cover" role="img" aria-label="Stack of The Wealth Compass books, cover showing the author holding a calculator"></div>

  <div class="offer">
    <h1 class="headline">Get instant access to your free resources</h1>
    <div class="rule"></div>
    <ul class="resource-list">
      <li>The Wealth Compass Checklist<svg class="tick" viewBox="0 0 18 14"><path d="M1 7l5 5L17 1" fill="none" stroke="var(--green-dark)" stroke-width="3"/></svg></li>
      <li>Financial Worksheets<svg class="tick" viewBox="0 0 18 14"><path d="M1 7l5 5L17 1" fill="none" stroke="var(--green-dark)" stroke-width="3"/></svg></li>
      <li>Database of Investment Tools<svg class="tick" viewBox="0 0 18 14"><path d="M1 7l5 5L17 1" fill="none" stroke="var(--green-dark)" stroke-width="3"/></svg></li>
    </ul>
    <div class="rule bottom"></div>
    <p class="resources-url">DariaFelt.com/Resources</p>
  </div>

  <div class="social">
    <p class="social-title">Don't forget to follow Daria Felt on social media:</p>
    <div class="social-grid">
      <span class="social-item"><span class="social-dot"></span>@dariafelt7</span>
      <span class="social-item"><span class="social-dot"></span>@thewealthcompassbook</span>
      <span class="social-item"><span class="social-dot"></span>@WealthCompassBk</span>
      <span class="social-item"><span class="social-dot"></span>@thewealthcompassbook</span>
    </div>
  </div>
</section>

<section class="postcard back">
  <div class="band"></div>

  <div class="pitch">
    <h2 class="pitch-headline">Want to work directly with Daria and The Wealth Compass team to help you make your money grow and stay safe?</h2>
    <p class="pitch-label">Work with us to</p>
    <ul class="service-list">
      <li>Hire Daria as a Keynote Speaker</li>
      <li>Teach Financial Literacy Workshops</li>
      <li>Receive Financial Coaching</li>
    </ul>
    <p class="services-cta">Want to learn more about how we can help?</p>
    <p class="services-url">DariaFelt.com/Services</p>
  </div>

  <div class="contact">
    <p class="contact-name">Daria Felt</p>
    <p class="contact-role">Author | Speaker | Investor</p>
    <p class="contact-line">daria@thewealthcompassbook.com</p>
    <p class="contact-line">416-555-0187</p>
  </div>

  <p class="brand-name">The Wealth Compass</p>

  <div class="portrait" role="img" aria-label="Photo of Daria Felt in a black blazer, hand on hip"></div>
</section>

</body>
</html>
```